Corporate Design für Sonderlösungen für Industrie und Handel
Zielgruppe
Wir entwickeln Sonderlösungen für Industrie und Handel. Unsere Kundschaft hat in der Regel ein existentes Problem oder eine Problemstellung, für das nach Lösungen gesucht wird. Hier kommen wir ins Spiel. Hauptsächlich sind diese Probleme im Bereich Logistik und Versand angesiedelt.
Aufgabenstellung
Hier sind sie relativ frei... das Corparate Indentity soll eine dynamische , moderne Komponente haben. Das Symsbol einen weitläufigen Bezug zu einem oder mehreren Begriffen wie Technik, Lösung , Logistik etc. haben.

```html
<!DOCTYPE html>
<html lang="de">
<head>
<meta charset="utf-8">
<title>Varlen GmbH &amp; Co KG – Visitenkarte</title>
<link rel="stylesheet" href="https://fonts.googleapis.com/css2?family=Montserrat:wght@400;600;700&display=swap">
<style>
  :root {
    --stage: #e6e8ea;
    --brand-blue: #1d95d8;
    --brand-navy: #12457a;
    --brand-green: #2ea84a;
    --text-dark: #333a40;
    --card-light: #ebebeb;
    --metal-1: #c9cdd1;
    --metal-2: #f2f3f4;
    --metal-3: #b3b8bd;
    --screw: #8d9297;
  }
  html, body {
    margin: 0;
    width: 1200px;
    height: 720px;
    overflow: hidden;
    background: var(--stage);
    font-family: "Montserrat", Arial, sans-serif;
  }
  .stage {
    position: relative;
    width: 1200px;
    height: 720px;
  }
  .card {
    position: absolute;
    top: 192px;
    width: 520px;
    height: 336px;
    box-sizing: border-box;
    box-shadow: 0 6px 18px rgba(0,0,0,0.18);
  }
  .card--front {
    left: 60px;
    background: linear-gradient(160deg, var(--metal-1) 0%, var(--metal-2) 30%, var(--metal-3) 52%, var(--metal-2) 74%, var(--metal-1) 100%);
  }
  .card--back {
    left: 620px;
    background: var(--card-light);
  }
  .screw {
    position: absolute;
    width: 12px;
    height: 12px;
    border-radius: 50%;
    background: radial-gradient(circle at 40% 35%, #d6d9dc, var(--screw));
    box-shadow: 0 1px 1px rgba(0,0,0,0.3);
  }
  .screw--tl { top: 16px; left: 16px; }
  .screw--tr { top: 16px; right: 16px; }
  .screw--bl { bottom: 16px; left: 16px; }
  .screw--br { bottom: 16px; right: 16px; }
  .nut {
    position: absolute;
    width: 12px;
    height: 12px;
    border-radius: 50%;
    background: #6e7378;
    box-shadow: inset 0 0 0 3px #9aa0a5;
  }
  .nut--tl { top: 16px; left: 16px; }
  .nut--tr { top: 16px; right: 16px; }
  .nut--bl { bottom: 16px; left: 16px; }
  .nut--br { bottom: 16px; right: 16px; }

  .front-brand {
    position: absolute;
    left: 0;
    right: 0;
    top: 148px;
    text-align: center;
    color: var(--brand-blue);
    font-weight: 700;
    font-size: 34px;
    line-height: 40px;
    white-space: nowrap;
  }

  .back-brand {
    position: absolute;
    left: 36px;
    top: 38px;
    color: var(--brand-navy);
    font-weight: 700;
    font-size: 16px;
    line-height: 20px;
    white-space: nowrap;
  }
  .accent-bar {
    position: absolute;
    width: 5px;
    background: var(--brand-navy);
  }
  .accent-bar--left { left: 0; top: 130px; height: 34px; }
  .accent-bar--right { right: 0; top: 236px; height: 34px; }

  .person {
    position: absolute;
    left: 36px;
    top: 130px;
  }
  .person__name {
    margin: 0;
    font-size: 19px;
    font-weight: 600;
    color: var(--brand-navy);
  }
  .person__role {
    margin: 2px 0 0;
    font-size: 14px;
    color: var(--text-dark);
  }

  .contact {
    position: absolute;
    right: 30px;
    top: 118px;
    text-align: right;
    color: var(--text-dark);
    font-size: 14px;
    line-height: 1.35;
  }
  .contact__row {
    display: flex;
    justify-content: flex-end;
    align-items: center;
    gap: 10px;
  }
  .contact__row + .contact__row { margin-top: 12px; }
  .contact__company {
    font-weight: 700;
    color: var(--brand-navy);
  }
  .contact__icon {
    flex: 0 0 auto;
    width: 18px;
    height: 18px;
  }
</style>
</head>
<body>
<main class="stage">

  <section class="card card--front" aria-label="Vorderseite">
    <span class="screw screw--tl"></span>
    <span class="screw screw--tr"></span>
    <span class="screw screw--bl"></span>
    <span class="screw screw--br"></span>
    <div class="front-brand">Varlen GmbH &amp; Co KG</div>
  </section>

  <section class="card card--back" aria-label="Rückseite">
    <span class="nut nut--tl"></span>
    <span class="nut nut--tr"></span>
    <span class="nut nut--bl"></span>
    <span class="nut nut--br"></span>
    <span class="accent-bar accent-bar--left"></span>
    <span class="accent-bar accent-bar--right"></span>

    <div class="back-brand">Varlen GmbH &amp; Co KG</div>

    <div class="person">
      <p class="person__name">Jonas Reimold</p>
      <p class="person__role">Geschäftsführer</p>
    </div>

    <div class="contact">
      <div class="contact__row">
        <div>
          <div class="contact__company">Varlen GmbH &amp; Co KG</div>
          <div>Lindenweg 12</div>
          <div>41061 Mönchberg</div>
        </div>
        <svg class="contact__icon" viewBox="0 0 18 18" aria-hidden="true">
          <circle cx="9" cy="9" r="9" fill="var(--brand-green)"/>
          <path d="M9 4a3 3 0 0 0-3 3c0 2.3 3 6 3 6s3-3.7 3-6a3 3 0 0 0-3-3z" fill="#fff"/>
          <circle cx="9" cy="7" r="1.1" fill="var(--brand-green)"/>
        </svg>
      </div>
      <div class="contact__row">
        <span>0049 (0) 2161-4827305</span>
        <svg class="contact__icon" viewBox="0 0 18 18" aria-hidden="true">
          <circle cx="9" cy="9" r="9" fill="var(--brand-green)"/>
          <path d="M6 4.5l1.6 2.2-1 1a6 6 0 0 0 3.7 3.7l1-1 2.2 1.6-1 1.5C9.8 13.7 4.3 8.2 4.5 5.5z" fill="#fff"/>
        </svg>
      </div>
      <div class="contact__row">
        <span>0049-176-58316092</span>
        <svg class="contact__icon" viewBox="0 0 18 18" aria-hidden="true">
          <circle cx="9" cy="9" r="9" fill="var(--brand-green)"/>
          <rect x="6.3" y="4" width="5.4" height="10" rx="1" fill="#fff"/>
          <rect x="7.2" y="5.2" width="3.6" height="6.2" fill="var(--brand-green)"/>
        </svg>
      </div>
      <div class="contact__row">
        <span>jr@varlen.de</span>
        <svg class="contact__icon" viewBox="0 0 18 18" aria-hidden="true">
          <circle cx="9" cy="9" r="9" fill="var(--brand-green)"/>
          <rect x="4.5" y="6" width="9" height="6.2" fill="#fff"/>
          <path d="M4.5 6l4.5 3.6L13.5 6" fill="none" stroke="var(--brand-green)" stroke-width="1"/>
        </svg>
      </div>
    </div>
  </section>

</main>
</body>
</html>
```